New Website

New website is to be the same as Copper Lantern.

Website needs to be fully functional, with only text and logo to be added by client at a later date.

Logo has been added for reference.

Reason: waiting for the final submissions to be completed.

```html
<!DOCTYPE html>
<html lang="en">
<head>
<meta charset="utf-8">
<title>ALDERA – steady paths to progress</title>
<link href="https://fonts.googleapis.com/css2?family=Libre+Baskerville:wght@400;700&family=Arimo:wght@400;700&family=Open+Sans:ital,wght@0,400;0,600;0,700;1,400&display=swap" rel="stylesheet">
<style>
:root{
  --page-bg:#3a3a3a;
  --white:#ffffff;
  --indigo:#3c4a9c;
  --indigo-dark:#323e8a;
  --sky:#74b3da;
  --sky-light:#8fc2e3;
  --button-blue:#5b7fb8;
  --text:#555a66;
  --rule:#e2e4e8;
}
*{margin:0;padding:0;box-sizing:border-box}
html,body{width:1200px;height:2965px;overflow:hidden}
body{background:var(--page-bg);font-family:"Arimo",Arial,sans-serif;color:var(--text);position:relative}
.site{position:absolute;left:99px;top:0;width:1002px;height:2965px;background:var(--white)}
.abs{position:absolute}

/* header */
.header{left:0;top:0;width:1002px;height:95px;border-top:3px solid var(--indigo);background:var(--white)}
.brand-square{left:26px;top:30px;width:30px;height:30px;background:var(--indigo)}
.brand-name{left:68px;top:27px;font-family:"Libre Baskerville",Georgia,serif;font-size:30px;line-height:36px;color:var(--indigo);letter-spacing:1px}
.nav{top:45px;font-family:"Libre Baskerville",Georgia,serif;font-size:11px;color:#333;letter-spacing:.2px;white-space:nowrap}
.nav.active{color:var(--indigo)}

/* hero */
.hero{left:0;top:95px;width:1002px;height:512px;background:linear-gradient(90deg,#eef1f3 0%,#f7f8f9 40%,#e9edf0 100%);overflow:hidden}
.hero-photo{left:470px;top:0;width:532px;height:512px;background:linear-gradient(160deg,#d8dde2 0%,#c2c7cc 40%,#2b2f36 75%,#3a3f48 100%)}
.hero-badge{left:802px;top:0;width:200px;height:36px;background:var(--sky-light);color:var(--white);font-family:"Libre Baskerville",Georgia,serif;font-size:11px;line-height:36px;padding-left:16px;white-space:nowrap}
.hero-title{left:98px;top:130px;font-family:"Libre Baskerville",Georgia,serif;font-weight:400;font-size:38px;line-height:46px;color:var(--indigo);letter-spacing:2px}
.hero-rule{left:98px;top:190px;width:362px;height:1px;background:#c7ccd4}
.hero-copy{left:98px;top:200px;width:380px;font-size:12px;line-height:22px;color:#555}
.hero-btn{left:96px;top:302px;width:170px;height:42px;background:var(--button-blue);border-bottom:4px solid var(--indigo);color:var(--white);font-family:"Libre Baskerville",Georgia,serif;font-size:11px;text-align:center;line-height:40px;white-space:nowrap}
.dots{left:98px;top:415px;display:flex;gap:6px}
.dots span{width:12px;height:12px;border-radius:50%;border:2px solid var(--button-blue)}
.dots span.on{background:var(--button-blue)}
.video-tab{left:742px;top:282px;width:211px;height:37px;background:var(--sky-light);color:#222;font-family:"Libre Baskerville",Georgia,serif;font-size:11px;line-height:37px;padding-left:46px;white-space:nowrap}
.video-tab svg{position:absolute;left:16px;top:9px}
.hero-panel{left:560px;top:319px;width:393px;height:146px;background:rgba(60,74,156,.9);color:var(--white);padding:18px 26px}
.hero-panel h3{font-family:"Open Sans",Arial,sans-serif;font-style:italic;font-weight:400;font-size:15px;margin-bottom:18px}
.hero-panel p{font-size:11.5px;line-height:20px;color:#b7c0e6}

/* welcome */
.welcome-title{left:0;top:660px;width:1002px;text-align:center;font-family:"Libre Baskerville",Georgia,serif;font-weight:400;font-size:24px;color:#222}
.welcome-title span{color:var(--indigo)}
.welcome-copy{left:20px;top:712px;width:962px;text-align:center;font-size:11px;line-height:23px;color:#555}
.divider{left:22px;top:815px;width:958px;height:1px;background:var(--rule)}
.video{left:22px;top:854px;width:958px;height:417px;background:linear-gradient(180deg,#5b93d8 0%,#3b6fc0 45%,#1d3f86 80%,#152d62 100%);box-shadow:0 14px 14px -10px rgba(0,0,0,.35)}
.play{left:457px;top:164px}

/* team */
.team{left:0;top:1345px;width:1002px;height:889px;background:var(--sky)}
.team-title{left:0;top:24px;width:1002px;text-align:center;font-family:"Libre Baskerville",Georgia,serif;font-weight:400;font-size:24px;color:var(--white)}
.team-rule{left:22px;top:78px;width:958px;height:1px;background:rgba(255,255,255,.6)}
.member{width:260px}
.member-photo{width:260px;height:255px;box-shadow:0 6px 10px rgba(0,0,0,.3)}
.photo-dark{background:linear-gradient(180deg,#5e5e5e 0%,#2b2b2b 100%)}
.photo-warm{background:linear-gradient(135deg,#7a6a60 0%,#3a302c 100%)}
.photo-light{background:linear-gradient(135deg,#e6e8ea 0%,#b9bdc2 100%)}
.member-name{margin-top:10px;text-align:center;color:var(--white);font-size:14px}
.member-role{text-align:center;color:#cfe3f1;font-size:11px;margin-top:2px}
.intro-card{width:283px;height:255px;background:var(--indigo);color:var(--white);text-align:center;padding:36px 30px;box-shadow:0 6px 10px rgba(0,0,0,.3)}
.intro-card h3{font-size:17px;line-height:22px;font-weight:700;margin-bottom:18px}
.intro-card p{font-size:11px;line-height:19px;color:#dfe4f6}
.social-squares{display:flex;gap:6px;justify-content:center;margin-top:20px}
.social-squares span{width:30px;height:30px;background:var(--indigo-dark);border:1px solid rgba(255,255,255,.25)}
.team-copy{left:60px;top:760px;width:882px;text-align:center;color:var(--white);font-size:11px;line-height:21px}
.team-btn{left:407px;top:819px;width:158px;height:40px;background:var(--indigo);color:var(--white);font-size:12px;line-height:40px;text-align:center}

/* services */
.services-title{left:0;top:2280px;width:1002px;text-align:center;font-family:"Libre Baskerville",Georgia,serif;font-weight:400;font-size:24px;color:#222}
.services-title span{color:var(--indigo)}
.service{width:230px;text-align:center}
.service-icon{width:114px;height:114px;margin:0 auto;border-radius:50%;border:5px solid var(--sky);background:var(--white);display:flex;align-items:center;justify-content:center;box-shadow:4px 6px 8px rgba(0,0,0,.2)}
.service-icon div{width:86px;height:86px;border-radius:50%;background:var(--sky);display:flex;align-items:center;justify-content:center}
.service h4{margin-top:20px;font-size:12px;color:var(--indigo);font-weight:700}
.service p{margin-top:10px;font-size:10.5px;line-height:18px;color:#555}
.read-more{display:inline-block;margin-top:12px;width:80px;height:30px;border:1px solid #b7cde3;color:var(--button-blue);font-size:10px;line-height:28px}

/* footer */
.footer{left:0;top:2630px;width:1002px;height:276px;background:var(--indigo);color:var(--white)}
.footer h5{position:absolute;top:36px;font-family:"Open Sans",Arial,sans-serif;font-weight:600;font-size:15px;letter-spacing:.3px}
.footer-nav{left:47px;top:70px;list-style:none;font-size:11px;line-height:21px;color:#d5dbf3}
.footer-nav li::before{content:"";display:inline-block;border-left:5px solid #d5dbf3;border-top:3px solid transparent;border-bottom:3px solid transparent;margin:0 12px 1px 0}
.footer-about{left:201px;top:72px;width:232px;font-size:11px;line-height:21px;color:#d5dbf3;text-align:justify}
.footer-news{left:480px;top:72px;width:240px;font-family:"Open Sans",Arial,sans-serif;font-style:italic;font-size:11px;line-height:20px;color:#b8c1e8}
.news-field{left:480px;top:133px;width:200px;height:36px;border:1px solid #8d98d4;color:#d5dbf3;font-size:10px;line-height:34px;padding-left:12px}
.news-go{left:680px;top:133px;width:40px;height:36px;background:var(--sky);display:flex;align-items:center;justify-content:center}
.legal{left:480px;top:184px;font-size:9px;color:#d5dbf3;text-decoration:underline}
.field{left:764px;width:198px;border:1px solid #8d98d4;color:#d5dbf3;font-size:10px;padding:8px 12px}
.submit-btn{left:909px;top:236px;width:56px;height:28px;background:var(--sky);font-size:10px;text-align:center;line-height:28px}
.bottom-bar{left:0;top:2906px;width:1002px;height:59px;background:var(--indigo-dark);color:var(--white)}
.copyright{left:47px;top:23px;font-size:11px}
.social-dots{right:40px;top:20px;display:flex;gap:16px}
.social-dots span{width:18px;height:18px;border-radius:50%;background:#c9d0ee}
</style>
</head>
<body>
<div class="site">

  <header class="header abs">
    <div class="brand-square abs"></div>
    <div class="brand-name abs">ALDERA</div>
    <a class="nav abs active" style="left:400px">HOME</a>
    <a class="nav abs" style="left:479px">ABOUT US</a>
    <a class="nav abs" style="left:584px">SERVICES</a>
    <a class="nav abs" style="left:683px">TEAM</a>
    <a class="nav abs" style="left:760px">TESTIMONIALS</a>
    <a class="nav abs" style="left:895px">CONTACT US</a>
  </header>

  <section class="hero abs">
    <div class="hero-photo abs" role="img" aria-label="Smiling businessman in a dark shirt in a bright office"></div>
    <div class="hero-badge abs">steady paths to progress</div>
    <h1 class="hero-title abs">ALDERA</h1>
    <div class="hero-rule abs"></div>
    <p class="hero-copy abs">Lorem ipsum dolor sit amet, consectetuer adipiscing elit. Aenean commodo ligula eget dolor. Aenean massa. Cum sociis natoque penatibus et magnis dis parturient montes nascetur.</p>
    <a class="hero-btn abs">MORE ABOUT ALDERA</a>
    <div class="dots abs"><span class="on"></span><span></span><span></span><span></span><span></span></div>
    <div class="video-tab abs">
      <svg width="18" height="18" viewBox="0 0 18 18"><circle cx="9" cy="9" r="9" fill="#1d1d1d"/><path d="M7 5l6 4-6 4z" fill="#fff"/></svg>
      WATCH THE VIDEO
    </div>
    <div class="hero-panel abs">
      <h3>Lorem ipsum dolor sit amet</h3>
      <p>Consectetuer adipiscing elit. Aenean commodo ligula eget dolor. Aenean massa. Cum sociis natoque penatibus et magnis dis parturient montes, nascetur ridiculus mus.</p>
    </div>
  </section>

  <h2 class="welcome-title abs">WELCOME TO <span>ALDERA</span></h2>
  <p class="welcome-copy abs">Lorem ipsum dolor sit amet, consectetuer adipiscing elit. Aenean commodo ligula eget dolor. Aenean massa. Cum sociis natoque penatibus et magnis dis parturient montes, nascetur ridiculus mus. Donec quam felis, ultricies nec, pellentesque eu, pretium quis, sem. Nulla consequat massa quis enim. Donec pede justo, fringilla vel, aliquet nec,<br>In enim justo, rhoncus ut, imperdiet a, venenatis vitae, justo. Nullam dictum felis eu pede mollis pretium.</p>
  <div class="divider abs"></div>

  <div class="video abs" role="img" aria-label="Video still of glass skyscrapers against a blue sky">
    <svg class="play abs" width="44" height="44" viewBox="0 0 44 44"><circle cx="22" cy="22" r="21" fill="#111" stroke="#fff" stroke-width="2"/><path d="M17 12l14 10-14 10z" fill="#fff"/></svg>
  </div>

  <section class="team abs">
    <h2 class="team-title abs">OUR TEAM</h2>
    <div class="team-rule abs"></div>

    <div class="member abs" style="left:70px;top:116px;width:283px">
      <div class="intro-card">
        <h3>Nemo enim ipsam voluptatem quia volupta</h3>
        <p>sit aspernatur aut odit aut fugit, sed quia consequuntur magni dolores eos qui ratione voluptatem sit aspern</p>
        <div class="social-squares"><span></span><span></span><span></span></div>
      </div>
      <div class="member-name">Ravi Sorell</div>
      <div class="member-role">Managing Director</div>
    </div>
    <div class="member abs" style="left:366px;top:116px">
      <div class="member-photo photo-dark" role="img" aria-label="Black and white portrait of a man in sunglasses and tie"></div>
      <div class="member-name">Marco Delane</div>
      <div class="member-role">Partner and Sole Director</div>
    </div>
    <div class="member abs" style="left:652px;top:116px">
      <div class="member-photo photo-warm" role="img" aria-label="Portrait of a man in a dark suit"></div>
      <div class="member-name">Idris Kalu</div>
      <div class="member-role">Associate Head of Communications</div>
    </div>

    <div class="member abs" style="left:78px;top:426px">
      <div class="member-photo photo-light" role="img" aria-label="Portrait of a man in a printed t-shirt"></div>
      <div class="member-name">Ravi Sorell</div>
      <div class="member-role">Managing Director</div>
    </div>
    <div class="member abs" style="left:366px;top:426px">
      <div class="member-photo photo-dark" role="img" aria-label="Black and white portrait of a man in sunglasses and tie"></div>
      <div class="member-name">Marco Delane</div>
      <div class="member-role">Partner and Sole Director</div>
    </div>
    <div class="member abs" style="left:652px;top:426px">
      <div class="member-photo photo-warm" role="img" aria-label="Portrait of a man in a dark suit"></div>
      <div class="member-name">Idris Kalu</div>
      <div class="member-role">Associate Head of Communications</div>
    </div>

    <p class="team-copy abs">Lorem ipsum dolor sit amet, consectetuer adipiscing elit. Aenean commodo ligula eget dolor. Aenean massa. Cum sociis natoque penatibus et magnis dis parturient montes, nascetur ridiculus mus. Donec quam felis, ultricies nec, pellentesque eu, pretium quis.</p>
    <a class="team-btn abs">SEE OUR TEAM &nbsp;&#187;</a>
  </section>

  <h2 class="services-title abs">OUR <span>SERVICES</span></h2>

  <div class="service abs" style="left:35px;top:2335px">
    <div class="service-icon"><div>
      <svg width="44" height="44" viewBox="0 0 44 44" fill="none" stroke="#fff" stroke-width="3"><rect x="6" y="10" width="26" height="26"/><path d="M18 28l2-7 16-16 5 5-16 16z" fill="#fff"/></svg>
    </div></div>
    <h4>LOREM IPSUM DOLOR</h4>
    <p>Lorem ipsum dolor sit amet, consectetuer adipiscing elit. Aenean commodo ligula eget dolor. Aenean massa. Cum</p>
    <a class="read-more">READ MORE</a>
  </div>
  <div class="service abs" style="left:268px;top:2335px">
    <div class="service-icon"><div>
      <svg width="48" height="40" viewBox="0 0 48 40" fill="#fff"><circle cx="14" cy="12" r="7"/><circle cx="34" cy="12" r="7"/><circle cx="24" cy="16" r="8"/><path d="M2 34c0-9 7-13 12-13s8 3 8 3-6 3-6 10zM46 34c0-9-7-13-12-13s-8 3-8 3 6 3 6 10zM10 38c0-9 6-14 14-14s14 5 14 14z"/></svg>
    </div></div>
    <h4>LOREM IPSUM DOLOR</h4>
    <p>Lorem ipsum dolor sit amet, consectetuer adipiscing elit. Aenean commodo ligula eget dolor. Aenean massa. Cum</p>
    <a class="read-more">READ MORE</a>
  </div>
  <div class="service abs" style="left:501px;top:2335px">
    <div class="service-icon"><div>
      <svg width="48" height="44" viewBox="0 0 48 44" fill="#fff" stroke="#fff" stroke-width="2"><circle cx="24" cy="7" r="5"/><circle cx="8" cy="36" r="5"/><circle cx="24" cy="36" r="5"/><circle cx="40" cy="36" r="5"/><path d="M24 12v12M8 31v-7h32v7M24 24v7" fill="none"/></svg>
    </div></div>
    <h4>LOREM IPSUM DOLOR</h4>
    <p>Lorem ipsum dolor sit amet, consectetuer adipiscing elit. Aenean commodo ligula eget dolor. Aenean massa. Cum</p>
    <a class="read-more">READ MORE</a>
  </div>
  <div class="service abs" style="left:737px;top:2335px">
    <div class="service-icon"><div>
      <svg width="46" height="42" viewBox="0 0 46 42" fill="#fff"><rect x="4" y="24" width="7" height="16"/><rect x="14" y="18" width="7" height="22"/><rect x="24" y="22" width="7" height="18"/><rect x="34" y="12" width="7" height="28"/><path d="M4 16l12-8 10 6 14-12" fill="none" stroke="#fff" stroke-width="2.5"/></svg>
    </div></div>
    <h4>LOREM IPSUM DOLOR</h4>
    <p>Lorem ipsum dolor sit amet, consectetuer adipiscing elit. Aenean commodo ligula eget dolor. Aenean massa. Cum</p>
    <a class="read-more">READ MORE</a>
  </div>

  <footer class="footer abs">
    <h5 style="left:47px">NAVIGATION</h5>
    <h5 style="left:201px">WHO WE ARE</h5>
    <h5 style="left:480px">SIGN UP FOR NEWSLETTER</h5>
    <h5 style="left:757px">NEED MORE INFO?</h5>
    <ul class="footer-nav abs">
      <li>Home</li><li>About</li><li>Who We Are</li><li>News</li><li>Services</li><li>Blog</li><li>News</li>
    </ul>
    <p class="footer-about abs">Lorem ipsum dolor sit amet, consectetuer adipiscing elit. Aenean commodo ligula eget dolor. Aenean massa. Cum sociis natoque penatibus et magnis dis parturient montes, nascetur ridiculus mus. Donec quam felis, ultricies nec, pellentesque eu...</p>
    <p class="footer-news abs">Sign up for our newsletter, and we'll keep you updated on all events at Northwind!</p>
    <div class="news-field abs">enter your email address</div>
    <div class="news-go abs"><svg width="10" height="12" viewBox="0 0 10 12"><path d="M2 1l6 5-6 5" fill="none" stroke="#fff" stroke-width="2"/></svg></div>
    <div class="legal abs">Terms of Use &nbsp;|&nbsp; Privacy Policy</div>
    <div class="field abs" style="top:82px;height:30px">NAME</div>
    <div class="field abs" style="top:122px;height:30px">EMAIL</div>
    <div class="field abs" style="top:162px;height:50px">MESSAGE</div>
    <div class="submit-btn abs">SUBMIT</div>
  </footer>

  <div class="bottom-bar abs">
    <div class="copyright abs">© Copyright 2014 &nbsp;Aldera &nbsp;| &nbsp;All rights reserved</div>
    <div class="social-dots abs"><span></span><span></span><span></span><span></span><span></span></div>
  </div>

</div>
</body>
</html>
```